Web design for Home Sleep Study clinic

We´re a group of Phisicians and working with patients with snoring e sleep apnea problems.
We´re beginning to offer home sleep studies (an option to lab studies) and we ´re building a webpage to share information, to find patients and to offer our product.
We already have a www adress and some idea about logo and brand.
We´re in Brazil and our service/webpage will be in Portuguese.

```html
<!DOCTYPE html>
<html lang="en">
<head>
<meta charset="utf-8">
<title>Home Sleep Study Clinic</title>
<link rel="stylesheet" href="https://fonts.googleapis.com/css2?family=PT+Sans:wght@400;700&family=Ubuntu:wght@400;700&display=swap">
<style>
  :root{
    --navy:#17506f;
    --navy-deep:#123f58;
    --green:#1d9a4f;
    --olive:#b7a010;
    --panel:#ece8e9;
    --ink:#222;
    --grey-line:#9a9a9a;
    --band:#dcdcdc;
    --field-line:#7fb0cf;
    --social:#f0a020;
    --social-grey:#8a8a8a;
  }
  *{margin:0;padding:0;box-sizing:border-box}
  html,body{width:941px;height:1200px;overflow:hidden;background:#fff}
  body{position:relative;font-family:"PT Sans",Arial,sans-serif;color:var(--ink)}
  .top-rule{position:absolute;left:0;top:0;width:941px;height:5px;background:var(--navy)}
  .nav-panel{position:absolute;left:0;top:5px;width:344px;height:187px;background:var(--panel)}
  .main-nav{position:absolute;left:145px;top:13px;width:199px;list-style:none}
  .main-nav li{height:25px;line-height:24px;padding-left:10px;font-size:11px;border-bottom:1px dotted #9a9a9a;color:#222}
  .main-nav li.active{background:var(--green);color:#fff;border-bottom:none;height:22px;line-height:22px;margin-bottom:3px}
  .main-nav li.large{font-size:14px}
  .connect{position:absolute;left:386px;top:18px;display:flex;align-items:center;gap:10px;font-size:14px;color:var(--navy-deep)}
  .social{display:flex;gap:3px}
  .social span{width:15px;height:15px;border-radius:50%;background:var(--social-grey)}
  .social span:first-child{background:var(--social)}
  .phone{font-size:21px;font-weight:700;color:var(--navy);letter-spacing:1px;margin-left:34px}
  .headline{position:absolute;left:386px;top:80px;font-size:36px;line-height:45px;font-weight:700;color:var(--navy);letter-spacing:3px}
  .rule-green{position:absolute;left:0;width:941px;height:6px;background:var(--green)}
  .hero{position:absolute;left:0;top:197px;width:941px;height:348px;background:linear-gradient(90deg,#3a3a3a 0%,#d8d8d8 22%,#9a9a9a 40%,#eeeeee 55%,#5a5a5a 72%,#e4e4e4 90%,#cfcfcf 100%)}
  .section-title{position:absolute;left:0;top:572px;width:941px;display:flex;align-items:center;gap:24px}
  .section-title::before,.section-title::after{content:"";flex:1;height:1px;background:var(--grey-line)}
  .section-title h2{font-size:31px;font-weight:700;color:var(--olive);letter-spacing:3px}
  .care-text{position:absolute;left:124px;top:630px;width:718px;font-size:10.4px;line-height:16.2px;letter-spacing:.35px;color:#333}
  .footer{position:absolute;left:0;top:999px;width:941px;height:164px;background:var(--navy);color:#fff}
  .who{position:absolute;left:74px;top:12px;width:428px}
  .who h3{font-size:17px;letter-spacing:2px;font-weight:700;margin-bottom:2px}
  .who p{font-size:10.2px;line-height:16px;letter-spacing:.3px}
  .touch{position:absolute;left:554px;top:18px;width:262px}
  .touch h3{font-family:"Ubuntu",Arial,sans-serif;font-weight:400;font-size:27px;margin-bottom:6px}
  .touch h3 b{font-weight:700}
  .field{display:block;height:20px;border:1px solid var(--field-line);margin:0 0 7px 4px;font-size:9px;line-height:18px;padding-left:7px;color:#b8d2e4}
  .send{position:absolute;left:789px;top:146px;font-size:10px;letter-spacing:.5px}
  .bottom-nav{position:absolute;left:0;top:1163px;width:941px;height:37px;background:var(--band);text-align:right;padding-right:20px;line-height:37px;font-size:19px;font-weight:700;letter-spacing:2.4px;color:var(--ink);white-space:nowrap}
</style>
</head>
<body>
  <div class="top-rule"></div>
  <div class="nav-panel"></div>
  <ul class="main-nav">
    <li class="active">HOME</li>
    <li>ABOUT US</li>
    <li>PRODUCTS</li>
    <li class="large">services</li>
    <li>WHY CHOOSE US?</li>
    <li>GALLERY</li>
    <li>Contact Us</li>
  </ul>

  <div class="connect">
    <span>Get Connected with us</span>
    <div class="social" aria-label="Social links"><span></span><span></span><span></span><span></span></div>
    <span class="phone">(021)5550198</span>
  </div>

  <h1 class="headline">Phisicians and working<br>with patients</h1>

  <div class="rule-green" style="top:191px"></div>
  <div class="hero" role="img" aria-label="Black and white photo of a woman covering her ears with a pillow while a man snores beside her in bed"></div>
  <div class="rule-green" style="top:545px"></div>

  <div class="section-title"><h2>we can care</h2></div>

  <p class="care-text">s simply dummy text of the printing and typesetting industry. Lorem Ipsum has been the industry's standard dummy text ever since the 1500s, when an unknown printer took a galley of type and scrambled it to make a type specimen book. It has survived not only five centuries, but also the leap into electronic typesetting, remaining essentially unchanged. It was popularised in the 1960s with the release of Letterfold sheets containing Lorem Ipsum passages, and more recently with desktop publishing software like Quill PageSetter including versions of Lorem Ipsum.s simply dummy text of the printing and typesetting industry. Lorem Ipsum has been the industry's standard dummy text ever since the 1500s, when an unknown printer took a galley of type and scrambled it to make a type specimen book. It has survived not only five centuries, but also the leap into electronic typesetting, remaining essentially unchanged. It was popularised in the 1960s with the release of Letterfold sheets containing Lorem Ipsum passages, and more recently with desktop publishing software like Quill PageSetter including versions of Lorem Ipsum.s simply dummy text of the printing and typesetting industry. Lorem Ipsum has been the industry's standard dummy text ever since the 1500s, when an unknown printer took a galley of type and scrambled it to make a type specimen book. It has survived not only five centuries, but also the leap into electronic typesetting, remaining essentially unchanged. It was popularised in the 1960s with the release of Letterfold sheets containing Lorem Ipsum passages, and more recently with desktop publishing software like Quill PageSetter including versions of Lorem Ipsum.s simply dummy text of the printing and typesetting industry. Lorem Ipsum has been the industry's standard dummy text ever since the 1500s, when an unknown printer took a galley of type and scrambled it to make a type specimen book. It has survived not only five centuries, but also the leap into electronic typesetting, remaining essentially unchanged. It was popularised in the 1960s with the release of Letterfold sheets containing Lorem Ipsum passages, and more recently with desktop publishing software like Quill PageSetter including versions of Lorem Ipsum.</p>

  <footer class="footer">
    <div class="who">
      <h3>WHO WE ARE</h3>
      <p>s simply dummy text of the printing and typesetting industry. Lorem Ipsum has been the industry's standard dummy text ever since the 1500s, when an unknown printer took a galley of type and scrambled it to make a type specimen book. It has survived not only five centuries, but also the leap into electronic typesetting, remaining essentially unchanged. It was popularised in the 1960s with the release of Letterfold sheets containing Lorem Ipsum passages</p>
    </div>
    <div class="touch">
      <h3>Get in <b>touch</b></h3>
      <span class="field">Name</span>
      <span class="field">Email</span>
      <span class="field">Details</span>
    </div>
    <span class="send">SEND</span>
  </footer>

  <nav class="bottom-nav">ABOUI US | PRODUCT | SERVIDES | WHY CHOOSEUS? | GALLERY | CONTACT UJS</nav>
</body>
</html>
```